Website re-design

We are a successful furnished apartment provider in Boston. We currently are working on re-designing our website www.bexlodging.com to make it more modern, designer look and user friendly. We hired a designer, but are not happy with the designs proposed and want to improve on them. The winning design will be paid regardless of whether we stay with our current designer or not. We want ideas and functional page links to see how it will work. Platform we have chosen is wordpress. Feel free to propose others easy for us to update and modify. We do not like Joomla on which website is currently running. We do not like flash nor long load times.
Please use photos on our website for design presentations. www.bexlodging.com

Target Market(s)

doctors, nurses, business men but mostly business women, some post-medical students

Industry/Entity Type

Apartment

Requirements
Must have
• Quick action button for reservation form and a notification and email forwarding system to us of reservation information by potential clients. Blog required with feedback by guests allowed, we can censor which are published. Slide shows of apartments.
Should not have
• No movies.

```html
<!DOCTYPE html>
<html lang="en">
<head>
<meta charset="utf-8">
<title>Bex Lodging Furnished Apartments</title>
<link href="https://fonts.googleapis.com/css2?family=Ubuntu:wght@400;500;700&family=PT+Sans:wght@400;700&display=swap" rel="stylesheet">
<style>
:root{
  --night:#1d2a3a;
  --night-deep:#121b27;
  --tan:#8c7856;
  --tan-light:#9a8663;
  --footer:#151515;
  --gold:#d9b76a;
  --orange:#e89a12;
  --orange-deep:#c46d06;
  --rust:#d4531f;
  --brown:#4d3322;
  --brown-title:#5b3a28;
  --cream:#f8f1e7;
  --panel:#f1f1f1;
  --white:#ffffff;
  --text:#3a3a3a;
  --muted:#8a8a8a;
  --link:#d4531f;
  --green:#5fa83a;
  --green-deep:#3f8a25;
}
*{box-sizing:border-box;margin:0;padding:0}
html,body{width:978px;height:1200px;overflow:hidden}
body{position:relative;background:var(--tan);font-family:"PT Sans",Arial,sans-serif;color:var(--text)}
a{text-decoration:none;color:inherit}
.night-band{position:absolute;left:0;top:0;width:978px;height:450px;background:linear-gradient(180deg,var(--night-deep),var(--night) 60%,#253447)}
.tan-band{position:absolute;left:0;top:450px;width:978px;height:668px;background:radial-gradient(ellipse at 50% 30%,var(--tan-light),var(--tan) 70%)}
.site-footer{position:absolute;left:0;top:1118px;width:978px;height:82px;background:var(--footer)}

.brand{position:absolute;left:122px;top:40px;display:flex;align-items:center;gap:8px}
.brand-dot{width:46px;height:46px;border-radius:50%;background:var(--gold)}
.brand-name{font-family:"Ubuntu",sans-serif;font-size:25px;color:var(--gold);letter-spacing:1px;line-height:1}
.brand-tag{font-family:"Ubuntu",sans-serif;font-size:9.5px;color:var(--gold);letter-spacing:2.2px;margin-top:3px}

.reserve-btn{position:absolute;left:665px;top:40px;width:188px;height:41px;border-radius:4px;background:linear-gradient(180deg,var(--green),var(--green-deep));border:1px solid #7cc25a;display:flex;align-items:center;padding-left:8px;font-family:"Ubuntu",sans-serif;font-weight:500;font-size:17px;color:var(--white);white-space:nowrap;text-shadow:0 1px 1px rgba(0,0,0,.4)}
.reserve-btn svg{position:absolute;right:10px;top:9px}

.main-nav{position:absolute;left:122px;top:114px;width:732px;height:29px;border-radius:15px;background:linear-gradient(180deg,#f5b52a,var(--orange) 55%,var(--orange-deep));box-shadow:0 2px 3px rgba(0,0,0,.5)}
.main-nav a{position:absolute;top:4px;font-family:"Ubuntu",sans-serif;font-size:15px;line-height:20px;color:var(--white);white-space:nowrap;text-shadow:0 1px 1px rgba(0,0,0,.3)}
.main-nav a.current{top:4px;left:5px;padding:0 10px;background:linear-gradient(180deg,#c84a12,#a33a0a);border-radius:11px}

.slideshow{position:absolute;left:124px;top:155px;width:729px;height:315px;background:var(--white);border-radius:6px;padding:6px;box-shadow:0 3px 8px rgba(0,0,0,.5)}
.slide-photo{width:100%;height:100%;border-radius:4px;background:linear-gradient(180deg,#d7c9a0 0%,#b8a57a 45%,#6b5138 75%,#3e3352 100%)}
.slide-arrow{position:absolute;top:302px;width:24px;height:24px}
.slide-arrow.prev{left:111px}
.slide-arrow.next{left:840px}

.welcome{position:absolute;left:122px;top:515px;width:732px;height:116px;background:var(--cream);border:1px solid #d8c8ae;box-shadow:0 1px 3px rgba(0,0,0,.3)}
.welcome-ribbon{position:absolute;left:142px;top:497px;width:692px;height:40px}
.welcome-title{position:absolute;left:142px;top:503px;width:692px;text-align:center;font-family:"Ubuntu",sans-serif;font-weight:400;font-size:23px;line-height:28px;color:var(--brown-title)}
.welcome-text{position:absolute;left:142px;top:546px;width:694px;font-size:10.5px;line-height:17.5px;letter-spacing:-.1px;color:var(--text)}
.like-btn{display:inline-flex;gap:4px;margin-left:28px;font-size:8.5px;line-height:11px;vertical-align:middle}
.like-btn span{border:1px solid #b8c1d6;background:#eef1f7;padding:0 4px;color:#3b5998}
.like-btn span.count{border-color:#ccc;background:var(--white);color:#333}

.section-title{position:absolute;left:122px;top:638px;width:732px;text-align:center;font-family:"Ubuntu",sans-serif;font-weight:700;font-size:26px;line-height:32px;color:var(--brown);text-shadow:0 1px 0 rgba(255,255,255,.25)}
.title-rule{position:absolute;top:658px;height:1px;background:rgba(80,55,30,.4)}

.apartments{position:absolute;left:122px;top:680px;width:732px;height:155px;background:var(--panel);box-shadow:0 1px 3px rgba(0,0,0,.3)}
.apt-card{position:absolute;top:701px;width:152px}
.apt-photo{margin:0 auto;width:144px;height:94px;border:3px solid var(--white);box-shadow:0 1px 2px rgba(0,0,0,.3)}
.apt-label{height:19px;background:var(--rust);color:var(--white);font-size:9px;text-align:center;line-height:19px}
.view-more{position:absolute;left:453px;top:827px;width:70px;height:18px;border-radius:9px;background:var(--white);border:1px solid #ccc;font-size:9px;color:#444;line-height:16px;padding-left:11px}
.view-more svg{position:absolute;right:3px;top:2px}

.info-panel{position:absolute;left:122px;top:862px;width:732px;height:241px;background:var(--white);border:3px solid #e8e8e8;box-shadow:0 1px 3px rgba(0,0,0,.4)}
.col-title{position:absolute;top:874px;font-family:"Ubuntu",sans-serif;font-weight:400;font-size:17px;line-height:20px;color:var(--rust);text-align:center;white-space:nowrap}
.col-rule{position:absolute;top:884px;height:1px;background:#d5d5d5}
.partner{position:absolute;width:108px;height:72px;border:1px solid #e0e0e0;padding:4px}
.partner div{width:100%;height:100%}
.tweet-list{position:absolute;left:374px;top:903px;width:230px;display:flex;flex-direction:column;gap:6px}
.tweet{font-size:9.5px;line-height:11.5px;color:#222;border-bottom:1px solid #e2e2e2;padding-bottom:4px}
.tweet a{color:var(--link)}
.tweet small{display:block;color:var(--muted);font-size:9px;line-height:11px}
.post{position:absolute;left:617px;width:230px;font-size:9.5px;line-height:12px;color:#222;border-bottom:1px solid #e2e2e2;padding-bottom:5px;text-transform:uppercase;white-space:nowrap}
.post small{display:block;color:var(--muted);font-size:8px;margin-top:1px}
.more-link{position:absolute;top:1078px;font-size:9.5px;color:var(--rust);white-space:nowrap}

.footer-nav{position:absolute;left:126px;top:1137px;display:flex;gap:20px;font-size:9.5px;color:#9a9a9a;white-space:nowrap}
.social-label{position:absolute;left:663px;top:1136px;font-size:11px;color:#bdbdbd}
.social{position:absolute;top:1132px;width:24px;height:24px;border-radius:3px}
.copyright{position:absolute;left:0;top:1178px;width:978px;text-align:center;font-size:8px;color:#5e5e5e}
</style>
</head>
<body>
<div class="night-band"></div>
<div class="tan-band"></div>
<div class="site-footer"></div>

<header>
  <div class="brand">
    <div class="brand-dot"></div>
    <div>
      <div class="brand-name">BEX LODGING</div>
      <div class="brand-tag">FURNISHED APARTMENTS</div>
    </div>
  </div>
  <a class="reserve-btn">Reservation Form
    <svg width="22" height="22" viewBox="0 0 22 22"><circle cx="11" cy="11" r="10" fill="#2f5d1c" stroke="#8fd06a"/><path d="M9 6l6 5-6 5z" fill="#9ad677"/></svg>
  </a>
  <nav class="main-nav">
    <a class="current">Home</a>
    <a style="left:89px">Apartments</a>
    <a style="left:205px">Reservations</a>
    <a style="left:327px">Blog</a>
    <a style="left:393px">Reviews</a>
    <a style="left:484px">Contact</a>
    <a style="left:574px">Boston</a>
    <a style="left:656px">About Us</a>
  </nav>
</header>

<section>
  <div class="slideshow"><div class="slide-photo" role="img" aria-label="Slide show photo of a furnished apartment bedroom with armchairs and a double bed"></div></div>
  <svg class="slide-arrow prev" viewBox="0 0 24 24"><circle cx="12" cy="12" r="11" fill="#fff"/><circle cx="12" cy="12" r="8" fill="#f08a12"/><path d="M14 8l-5 4 5 4z" fill="#fff"/></svg>
  <svg class="slide-arrow next" viewBox="0 0 24 24"><circle cx="12" cy="12" r="11" fill="#fff"/><circle cx="12" cy="12" r="8" fill="#f08a12"/><path d="M10 8l5 4-5 4z" fill="#fff"/></svg>
</section>

<section>
  <div class="welcome"></div>
  <svg class="welcome-ribbon" viewBox="0 0 692 40">
    <path d="M0 0H692L680 20L692 40H0L12 20Z" fill="#efd9b4"/>
    <path d="M23 12l2.4 5h5.4l-4.4 3.3 1.7 5.3-5.1-3.3-5.1 3.3 1.7-5.3-4.4-3.3h5.4z" fill="#4d3322"/>
    <path d="M669 12l2.4 5h5.4l-4.4 3.3 1.7 5.3-5.1-3.3-5.1 3.3 1.7-5.3-4.4-3.3h5.4z" fill="#4d3322"/>
  </svg>
  <h1 class="welcome-title">Welcome to Bex Lodging Furnished Apartments</h1>
  <p class="welcome-text">Bex Lodging is proud to offer some of the best furnished apartments in Boston. Our locations are in the trendiest area of the city: the South End. In the South End neighborhood, you will find wonderful restaurants, theaters, cafes and artist lofts. Our short term and extended stay apartments are very, very clean. We also offer the latest designer layouts: hardwood floors, Wireless Dsl, Cable TV, flat screen in most apartments, washer and dryer, cookware, cotton linens. Please click links on left for photo galleries, pricing, availability and reservation form and write us for more information. Thank you.<span class="like-btn"><span>Like</span><span class="count">86</span></span></p>
</section>

<section>
  <div class="title-rule" style="left:122px;width:280px"></div>
  <div class="title-rule" style="left:574px;width:280px"></div>
  <h2 class="section-title">Apartments</h2>
  <div class="apartments"></div>
  <div class="apt-card" style="left:137px"><div class="apt-photo" role="img" aria-label="Photo of Deluxe Apartment T5" style="background:linear-gradient(160deg,#e8d3a6,#b98a52 60%,#7a5a38)"></div><div class="apt-label">Deluxe Apartment T5</div></div>
  <div class="apt-card" style="left:320px"><div class="apt-photo" role="img" aria-label="Photo of Deluxe Apartment W5" style="background:linear-gradient(160deg,#d99a55,#b8652e 55%,#5e3a22)"></div><div class="apt-label">Deluxe Apartment W5</div></div>
  <div class="apt-card" style="left:503px"><div class="apt-photo" role="img" aria-label="Photo of Deluxe apartment T6" style="background:linear-gradient(160deg,#d8d0bc,#7a6a52 55%,#3f5f8a)"></div><div class="apt-label">Deluxe apartment T6</div></div>
  <div class="apt-card" style="left:686px"><div class="apt-photo" role="img" aria-label="Photo of Bohemian apartment W13" style="background:linear-gradient(160deg,#f0ece2,#c9c2b2 55%,#7a6d5c)"></div><div class="apt-label">Bohemian apartment W13</div></div>
  <a class="view-more">View more
    <svg width="12" height="12" viewBox="0 0 12 12"><circle cx="6" cy="6" r="6" fill="#4a3a4a"/><path d="M5 3.5l3 2.5-3 2.5z" fill="#fff"/></svg>
  </a>
</section>

<section>
  <div class="info-panel"></div>

  <div class="col-rule" style="left:130px;width:40px"></div><div class="col-rule" style="left:316px;width:42px"></div>
  <h3 class="col-title" style="left:170px;width:146px">Our Link Partners</h3>
  <div class="partner" style="left:129px;top:906px"><div style="background:linear-gradient(180deg,#5a5048,#2e2824)"></div></div>
  <div class="partner" style="left:250px;top:906px"><div style="background:#f4f4f4"></div></div>
  <div class="partner" style="left:129px;top:989px"><div style="background:#f4f4f4"></div></div>
  <div class="partner" style="left:250px;top:989px"><div style="background:#f4f4f4"></div></div>
  <span class="more-link" style="left:309px">View more ›</span>

  <div class="col-rule" style="left:374px;width:55px"></div><div class="col-rule" style="left:546px;width:56px"></div>
  <h3 class="col-title" style="left:429px;width:117px">Latest Tweets</h3>
  <div class="tweet-list">
    <div class="tweet">Dale Porter on Why You Should Never Listen to Your Customers <a>http://bx.co/EuTfwLuF</a> via @bizmagazine<small>4 day(s) ago from Share Button</small></div>
    <div class="tweet">I posted a new photo to PhotoNook <a>http://bx.co/wgcCNah9</a><small>5 day(s) ago from PhotoNook</small></div>
    <div class="tweet">We continuously improve our design and look. See these photos of today and one year ago... <a>http://bx.co/ruX0Nhus</a><small>5 day(s) ago from PhotoNook</small></div>
    <div class="tweet">Design and decor evolution at Bex Lodging <a>http://bx.co/AFlptdvk</a><small>5 day(s) ago from PhotoNook</small></div>
  </div>
  <span class="more-link" style="left:511px">Follow me on Chirper ›</span>

  <div class="col-rule" style="left:618px;width:72px"></div><div class="col-rule" style="left:775px;width:72px"></div>
  <h3 class="col-title" style="left:690px;width:85px">Our Blog</h3>
  <div class="post" style="top:907px">Corporate apartment design evolution<small>TUESDAY, 10 JANUARY 2012 21:27</small></div>
  <div class="post" style="top:947px">Corporate housing Boston - Bex Lodging<small>TUESDAY, 10 JANUARY 2012 21:27</small></div>
  <div class="post" style="top:986px">Pumpkin morning in Yarmouth, MA - Bex Lodging<small>THURSDAY, 27 OCTOBER 2011 14:48</small></div>
  <div class="post" style="top:1025px">Pumpkin morning in Yarmouth, MA - Bex Lodging<small>THURSDAY, 27 OCTOBER 2011 14:48</small></div>
  <span class="more-link" style="left:797px">Read more ›</span>
</section>

<footer>
  <nav class="footer-nav"><a>Home</a><a>Apartments</a><a>Reservations</a><a>Blog</a><a>Reviews</a><a>Contact</a><a>Boston</a><a>About Us</a></nav>
  <span class="social-label">We Are Social</span>
  <div class="social" style="left:740px;background:#3b5a98"></div>
  <div class="social" style="left:768px;background:#4aa8d8"></div>
  <div class="social" style="left:796px;background:#6aa82e"></div>
  <div class="social" style="left:824px;background:#d0231b"></div>
  <p class="copyright">© 2012 BEX LODGING 2010 - ALL RIGHTS RESERVED</p>
</footer>
</body>
</html>
```